Home Care company needs letter head branding

Home care company needs a letter head which can be used for all documents the company's clients view. We provided in home care for the elderly. We would like to use our company colors (2785A7, 0A4057 and 34A74D) and should not be too large as we will be using it on more than just a letter head but all documents our clients sign / receive.
Target Market(s)
Professional business
Industry/Entity Type
Health Care
Requirements
Must have
- corporate brand colors

```html
<!DOCTYPE html>
<html lang="en">
<head>
<meta charset="utf-8">
<title>Maplebrook Care – Letterhead &amp; Envelope</title>
<link href="https://fonts.googleapis.com/css2?family=Lato:wght@400;700&family=Arimo:wght@700&display=swap" rel="stylesheet">
<style>
  :root {
    --brand-blue: #2785A7;
    --brand-navy: #0A4057;
    --brand-green: #A9CC3A;
    --ink: #222;
    --paper: #ffffff;
    --backdrop: #d9dadc;
  }
  * { box-sizing: border-box; margin: 0; padding: 0; }
  html, body { width: 800px; height: 1200px; overflow: hidden; }
  body { background: var(--backdrop); font-family: "Lato", Arial, sans-serif; color: var(--ink); position: relative; }

  .sheet { position: absolute; background: var(--paper); overflow: hidden; }
  .letterhead { left: 128px; top: 74px; width: 544px; height: 704px; }
  .envelope { left: 53px; top: 857px; width: 694px; height: 304px; }

  .swoosh { position: absolute; left: 0; top: 0; }

  .brand { position: absolute; display: flex; align-items: center; gap: 10px; }
  .brand-dot { border-radius: 50%; border: 3px solid var(--brand-blue); background: var(--paper); flex: none; }
  .brand-name { font-family: "Lato", Arial, sans-serif; font-weight: 700; color: var(--brand-blue); white-space: nowrap; }
  .letterhead .brand { left: 138px; top: 40px; }
  .letterhead .brand-dot { width: 60px; height: 60px; }
  .letterhead .brand-name { font-size: 30px; }
  .envelope .brand { left: 222px; top: 30px; }
  .envelope .brand-dot { width: 54px; height: 54px; }
  .envelope .brand-name { font-size: 28px; }

  .contact { position: absolute; text-align: center; font-family: "Arimo", Arial, sans-serif; font-weight: 700; color: var(--brand-blue); }
  .contact .web { display: block; }
  .letterhead .contact { left: 172px; width: 200px; top: 97px; font-size: 10px; line-height: 12px; }
  .letterhead .contact .web { margin-top: 12px; }
  .envelope .contact { left: 197px; width: 300px; top: 106px; font-size: 13px; line-height: 14.5px; }
  .envelope .contact .web { margin-top: 15px; }

  .letter-body { position: absolute; left: 58px; top: 214px; width: 428px; font-size: 10.4px; line-height: 16.55px; text-align: justify; color: var(--ink); }

  .signature { position: absolute; left: 348px; top: 540px; width: 138px; height: 26px; border-radius: 4px; background: linear-gradient(90deg, rgba(169,204,58,0.15), rgba(169,204,58,0.45)); }
  .signatory { position: absolute; right: 58px; top: 570px; font-size: 11px; font-weight: 700; color: var(--ink); }

  .footer { position: absolute; display: flex; align-items: center; font-size: 9.6px; color: var(--ink); white-space: nowrap; }
  .footer .links span + span::before { content: "|"; font-weight: 700; margin: 0 4px; }
  .footer .divider { width: 1px; height: 22px; background: var(--ink); margin: 0 8px; }
  .footer .notes { font-size: 8.8px; }
  .footer .notes i { display: inline-block; width: 5px; height: 5px; border-radius: 50%; background: var(--brand-green); margin: 0 3px; vertical-align: 1px; }
  .envelope .footer .notes i { background: var(--ink); }
  .letterhead .footer { left: 58px; top: 659px; }
  .envelope .footer { left: 133px; top: 266px; }
</style>
</head>
<body>

<section class="sheet letterhead">
  <svg class="swoosh" width="80" height="620" viewBox="0 0 80 620" aria-hidden="true">
    <path d="M36,0 C22,120 22,270 52,460 C32,280 30,120 44,0 Z" fill="var(--brand-blue)"/>
    <path d="M12,0 C62,110 68,280 12,612 C56,270 52,110 28,0 Z" fill="var(--brand-green)"/>
  </svg>

  <div class="brand">
    <span class="brand-dot"></span>
    <span class="brand-name">Maplebrook Care</span>
  </div>

  <address class="contact">
    418 Elm Street, Suite B<br>
    Ashford, England 204560<br>
    Phone: 555-214-7730<br>
    Fax: 555-214-7731
    <span class="web">maplebrookcare.example</span>
  </address>

  <p class="letter-body">Lorem ipsum dolor sit amet, consectetur adipiscing elit. Donec eget nisi eget tortor iaculis tristique. Aliquam tincidunt posuere tortor hendrerit elementum. Nunc laoreet lorem a sem auctor fringilla. Pellentesque dignissim accumsan lobortis. Sed pharetra erat vitae dui imperdiet quis commodo orci dapibus. Cum sociis natoque penatibus et magnis dis parturient montes, nascetur ridiculus mus. Fusce at nunc libero. Nam met us lorem, rhoncus ac mattis ornare, blandit vel risus. Lorem ipsum dolor sit amet, consectetur adipiscing elit. Donec eget nisi eget tortor iaculis tristique. Aliquam tincidunt posuere tortor hendrerit elementum. Nunc laoreet lorem a sem auctor fringilla. Pellentesque dignissim accumsan lobortis. Sed pharetra erat vitae dui imperdiet quis commodo orci dapibus. Cum sociis natoque penatibus et magnis dis parturient montes, nascetur ridiculus mus. Fusce at nunc libero. Nam met us lorem, rhoncus ac mattis ornare, blandit vel risus. Lorem ipsum dolor sit amet, consectetur adipiscing elit. Donec eget nisi eget tortor iaculis tristique. Aliquam tincidunt posuere tortor hendrerit elementum. Nunc laoreet lorem a sem auctor fringilla. Pellentesque dignissim accumsan lobortis. Sed pharetra erat vitae dui imperdiet quis commodo orci dapibus. Cum sociis natoque penatibus et magnis dis parturient montes, nascetur ridiculus mus. Fusce at nunc libero. Nam met us lorem, rhoncus ac mattis ornare, blandit vel risus.</p>

  <div class="signature" role="img" aria-label="Handwritten signature of Evan Harlow in green ink"></div>
  <p class="signatory">Founder &amp; CEO</p>

  <footer class="footer">
    <span class="links"><span>Lorem Ipsum</span><span>Lorem Ipsum</span><span>Lorem Ipsum</span></span>
    <span class="divider"></span>
    <span class="notes">dolor sit amet<i></i>dolor sit amet<i></i>dolor sit amet</span>
  </footer>
</section>

<section class="sheet envelope">
  <svg class="swoosh" width="80" height="304" viewBox="0 0 80 304" aria-hidden="true">
    <path d="M52,0 C36,70 40,160 70,245 C50,160 48,70 62,0 Z" fill="var(--brand-blue)"/>
    <path d="M28,0 C78,70 74,170 32,304 C66,170 62,70 44,0 Z" fill="var(--brand-green)"/>
  </svg>

  <div class="brand">
    <span class="brand-dot"></span>
    <span class="brand-name">Maplebrook Care</span>
  </div>

  <address class="contact">
    418 Elm Street, Suite B<br>
    Ashford, England 204560<br>
    Phone: 555-214-7730<br>
    Fax: 555-214-7731
    <span class="web">maplebrookcare.example</span>
  </address>

  <footer class="footer">
    <span class="links"><span>Lorem Ipsum</span><span>Lorem Ipsum</span><span>Lorem Ipsum</span></span>
    <span class="divider"></span>
    <span class="notes">dolor sit amet<i></i>dolor sit amet<i></i>dolor sit amet</span>
  </footer>
</section>

</body>
</html>
```